Corvane Strategy Partners Marketing Audit Teaser

Design a 1-page (2-sided) teaser on the Corvane Strategy Partners Marketing Audit. A Project Brief; Copy document; logo file; and picture file will be provided to further detail what is required. Additional logo files are available, if needed, depending on the designers recommendations.

```html
<!DOCTYPE html>
<html lang="en">
<head>
<meta charset="utf-8">
<title>Corvane Strategy Partners Marketing Audit Teaser</title>
<link rel="stylesheet" href="https://fonts.googleapis.com/css2?family=Inter:wght@400;500;600;700&display=swap">
<style>
  :root {
    --navy: #1d3a4f;
    --orange: #e8683f;
    --ink: #24323d;
    --muted: #6f7f8b;
    --paper: #ffffff;
    --backdrop: #e3e3e4;
    --rule: #c9d0d6;
  }
  * { box-sizing: border-box; margin: 0; padding: 0; }
  html, body { width: 1200px; height: 1200px; overflow: hidden; }
  body {
    background: var(--backdrop);
    font-family: "Inter", Arial, sans-serif;
    color: var(--ink);
    position: relative;
  }
  .sheet {
    position: absolute;
    top: 232px;
    width: 520px;
    height: 735px;
    background: var(--paper);
    box-shadow: 0 14px 36px rgba(0,0,0,0.12);
    overflow: hidden;
  }
  .sheet--front { left: 60px; padding: 0 44px; }
  .sheet--back { left: 620px; display: flex; flex-direction: column; }

  /* Front */
  .brand { display: flex; align-items: center; gap: 12px; padding-top: 58px; height: 118px; }
  .brand__mark { width: 26px; height: 26px; background: var(--orange); flex: none; }
  .brand__name { font-size: 17px; font-weight: 600; color: var(--navy); line-height: 1.2; }
  .rule-short { width: 200px; height: 1px; background: var(--navy); opacity: .5; margin-top: 14px; }
  .headline {
    margin-top: 40px;
    font-size: 62px;
    font-weight: 700;
    line-height: 1.08;
    color: var(--navy);
    letter-spacing: -0.5px;
  }
  .headline__accent { color: var(--orange); display: block; }
  .intro { margin-top: 36px; font-size: 15px; line-height: 1.5; color: var(--ink); }
  .summary { margin-top: 16px; font-size: 15px; line-height: 1.5; color: var(--muted); }
  .front-foot {
    position: absolute; left: 44px; right: 44px; bottom: 0; height: 112px;
    border-top: 1px solid var(--rule);
    display: flex; align-items: center;
  }
  .front-foot::before {
    content: ""; position: absolute; top: -1px; right: 0; width: 50%; height: 1px; background: var(--orange);
  }
  .front-foot__col { flex: 1; padding-left: 24px; font-size: 15px; line-height: 1.45; }
  .front-foot__col + .front-foot__col { border-left: 1px solid var(--rule); }
  .front-foot__label { color: var(--navy); font-weight: 500; }
  .front-foot__label--accent { color: var(--orange); }

  /* Back */
  .back-top { height: 130px; flex: none; display: flex; align-items: center; padding: 0 30px; }
  .back-top__col { flex: 1; font-size: 21px; font-weight: 600; color: var(--navy); line-height: 1.2; padding: 0 16px; }
  .back-top__col + .back-top__col { border-left: 1px solid var(--rule); }
  .back-intro { height: 180px; flex: none; background: var(--navy); color: #fff; padding: 28px 34px; }
  .back-intro__title { font-size: 16px; font-weight: 600; margin-bottom: 10px; }
  .back-intro__body { font-size: 12.5px; line-height: 1.55; color: #cfdae2; }
  .back-photo {
    height: 210px; flex: none;
    background: linear-gradient(135deg, #e9ecef 0%, #c9d3db 55%, #8b9aa6 100%);
  }
  .back-claim {
    height: 120px; flex: none; background: var(--navy); color: #fff;
    padding: 18px 34px; font-size: 22px; font-weight: 600; line-height: 1.25;
  }
  .back-cta {
    flex: 1; background: linear-gradient(90deg, #d85a34, var(--orange));
    display: flex; align-items: center; padding: 0 30px; gap: 22px; color: #fff;
  }
  .back-cta__icon { width: 40px; height: 40px; border: 4px solid rgba(255,255,255,.8); flex: none; }
  .back-cta__text { border-left: 1px solid rgba(255,255,255,.5); padding-left: 22px; }
  .back-cta__title { font-size: 17px; font-weight: 600; text-transform: uppercase; letter-spacing: .5px; }
  .back-cta__body { font-size: 10.5px; line-height: 1.45; margin-top: 4px; color: #ffe3d8; }
</style>
</head>
<body>
  <section class="sheet sheet--front">
    <header class="brand">
      <span class="brand__mark"></span>
      <span class="brand__name">Corvane Strategy Partners</span>
    </header>
    <div class="rule-short"></div>
    <h1 class="headline">Profit Growth Marketing <span class="headline__accent">Audit</span></h1>
    <p class="intro">Discover where your budget, channels and messaging are working and where they fall short. Our independent review examines every touchpoint, benchmarks results against your market and delivers a clear, prioritised action plan that your team can put to work immediately.</p>
    <p class="summary">A focused audit that reveals hidden opportunities and turns marketing spend into measurable growth.</p>
    <footer class="front-foot">
      <div class="front-foot__col"><span class="front-foot__label">Project brief</span><br>Findings in four weeks</div>
      <div class="front-foot__col"><span class="front-foot__label front-foot__label--accent">Consultation First</span><br>Independent insight</div>
    </footer>
  </section>

  <section class="sheet sheet--back">
    <div class="back-top">
      <div class="back-top__col">Wider<br>Perspectives</div>
      <div class="back-top__col">Clear Growth<br>Evaluation</div>
    </div>
    <div class="back-intro">
      <p class="back-intro__title">See exactly where your marketing budget goes</p>
      <p class="back-intro__body">We map every channel, campaign and cost, then show which activities drive revenue and which quietly drain it. The result is a plain, practical view of performance.</p>
    </div>
    <div class="back-photo" role="img" aria-label="Photo of two consultants smiling at a table with a laptop in a bright office"></div>
    <div class="back-claim">Clear thinking<br>that drives<br>lasting growth</div>
    <div class="back-cta">
      <span class="back-cta__icon"></span>
      <div class="back-cta__text">
        <p class="back-cta__title">Book your audit</p>
        <p class="back-cta__body">Start with a free consultation and receive a tailored proposal within five working days of our first call.</p>
      </div>
    </div>
  </section>
</body>
</html>
```